Tellborne Medical

Need smart and sleek business cards design for my medical distribution company. use logos attached.

add my details

Lorcan Pettifer
Director/Sales Agent
lorcan@tellbornemedical-example.com.au
0491 638 170

```html
<!DOCTYPE html>
<html lang="en">
<head>
<meta charset="utf-8">
<title>Tellborne Medical – Business Cards</title>
<link href="https://fonts.googleapis.com/css2?family=Montserrat:wght@400;600;700&display=swap" rel="stylesheet">
<style>
  :root {
    --bg: #2b2b2d;
    --navy: #1f2a5e;
    --sky: #2a8bc2;
    --white: #ffffff;
    --ink-soft: #dfe6f5;
  }
  * { box-sizing: border-box; margin: 0; padding: 0; }
  html, body { width: 1200px; height: 875px; overflow: hidden; }
  body {
    background: var(--bg);
    font-family: "Montserrat", sans-serif;
    display: flex;
    align-items: center;
    justify-content: center;
    gap: 60px;
  }
  .card {
    width: 510px;
    height: 292px;
    border-radius: 18px;
    position: relative;
    overflow: hidden;
  }
  .card--back {
    background: var(--navy);
    display: flex;
    align-items: center;
    justify-content: center;
  }
  .card--front { background: var(--white); }

  .wordmark {
    font-weight: 700;
    font-size: 34px;
    letter-spacing: 1px;
    text-transform: uppercase;
    line-height: 1;
    display: flex;
    align-items: center;
    gap: 12px;
  }
  .wordmark__square { width: 22px; height: 22px; flex: none; }
  .card--back .wordmark { color: var(--white); }
  .card--back .wordmark__square { background: var(--white); }

  .card--front .wordmark {
    position: absolute;
    top: 62px;
    right: 40px;
    color: var(--navy);
  }
  .card--front .wordmark__square { background: var(--navy); }

  .band {
    position: absolute;
    top: 168px;
    height: 58px;
    display: flex;
    flex-direction: column;
    justify-content: center;
  }
  .band--name {
    left: 0;
    width: 250px;
    background: var(--navy);
    color: var(--white);
    align-items: flex-end;
    padding-right: 18px;
  }
  .person__name { font-weight: 700; font-size: 18px; }
  .person__role { font-weight: 400; font-size: 10px; color: var(--ink-soft); margin-top: 2px; }

  .band--contact {
    left: 250px;
    right: 0;
    background: var(--sky);
    color: var(--white);
    padding-left: 14px;
    gap: 5px;
    font-size: 9.5px;
  }
  .contact { display: flex; align-items: center; gap: 7px; }
  .contact svg { width: 10px; height: 10px; flex: none; fill: var(--white); }
</style>
</head>
<body>
  <section class="card card--back">
    <div class="wordmark"><span class="wordmark__square"></span>Tellborne Medical</div>
  </section>

  <section class="card card--front">
    <div class="wordmark"><span class="wordmark__square"></span>Tellborne Medical</div>

    <div class="band band--name">
      <p class="person__name">Lorcan Pettifer</p>
      <p class="person__role">Director/Sales Agent</p>
    </div>

    <div class="band band--contact">
      <p class="contact">
        <svg viewBox="0 0 24 24" aria-hidden="true"><path d="M6.6 10.8a15 15 0 0 0 6.6 6.6l2.2-2.2c.3-.3.7-.4 1-.2 1.1.4 2.3.6 3.6.6.6 0 1 .4 1 1V20c0 .6-.4 1-1 1A17 17 0 0 1 3 4c0-.6.4-1 1-1h3.5c.6 0 1 .4 1 1 0 1.3.2 2.5.6 3.6.1.3 0 .7-.2 1z"/></svg>
        0491 638 170
      </p>
      <p class="contact">
        <svg viewBox="0 0 24 24" aria-hidden="true"><path d="M2 5h20v14H2z M3.5 6.5 12 13l8.5-6.5" fill="none" stroke="#fff" stroke-width="2"/></svg>
        lorcan@tellbornemedical-example.com.au
      </p>
    </div>
  </section>
</body>
</html>
```